Business Card Design for company

We want new business cards. We'd like something different-- yet still highly professional. Our tagline is Providing leadership, delivering success. Stock photos are ok, as long as they are relevant and look upscale.

Target Market(s)

Architecture/Business Management Consulting/Engineering Consulting

Contact Information for Business Card

dark gray background with pops of blue might be good, but you tell me. You're the designers. Rounded corners might be nice, but again, you tell me.

Font styles to use
Serif
Sans Serif

Colors
3276b5
5c5c5c
9d9d9d
fbfbfb

Requirements
Nice to have
• Something different, but still very professional.

```html
<!DOCTYPE html>
<html lang="en">
<head>
<meta charset="utf-8">
<title>Norvane Group — Business Card</title>
<link rel="stylesheet" href="https://fonts.googleapis.com/css2?family=Saira:wght@400;500;600&display=swap">
<style>
  :root {
    --blue: #3276b5;
    --blue-deep: #1f5c96;
    --gray: #5c5c5c;
    --gray-light: #9d9d9d;
    --paper: #fbfbfb;
    --stage: #333333;
    --white: #ffffff;
  }
  * { box-sizing: border-box; margin: 0; padding: 0; }
  html, body {
    width: 1200px; height: 1112px; overflow: hidden;
    background: var(--white);
    font-family: "Saira", sans-serif;
  }
  .stage {
    position: absolute; inset: 0;
    background: var(--stage);
    border-radius: 32px;
  }
  .card {
    position: absolute; left: 287px; width: 582px; height: 359px;
    border-radius: 32px; overflow: hidden;
    background: var(--white);
  }
  .card--front { top: 133px; }
  .card--back { top: 576px; }

  .brand {
    color: var(--blue-deep);
    font-weight: 600;
    letter-spacing: 0.04em;
    line-height: 1;
    text-transform: uppercase;
  }
  .card--front .brand {
    position: absolute; left: 33px; top: 50px;
    font-size: 26px; width: 150px;
  }

  .holder {
    position: absolute; right: 29px; top: 64px; text-align: right;
  }
  .holder__name {
    color: var(--gray); font-size: 29px; font-weight: 500;
    line-height: 1; letter-spacing: 0.01em;
  }
  .holder__title {
    color: var(--blue); font-size: 11px; font-weight: 500;
    letter-spacing: 0.03em; margin-top: 2px;
  }

  .skyline-band {
    position: absolute; left: 0; top: 153px; width: 100%; height: 73px;
    background: linear-gradient(90deg, #8fa9c8 0%, #5f83ad 35%, #2c4f7d 60%, #7f9cc0 80%, #3b5f8c 100%);
  }

  .pin { position: absolute; top: 190px; width: 40px; height: 52px; }

  .contact {
    position: absolute; top: 263px;
    color: var(--gray); font-size: 12px; line-height: 15px;
    letter-spacing: 0.02em; text-transform: uppercase;
  }
  .contact--phone { left: 32px; }
  .contact--email { left: 175px; width: 200px; text-align: center; }
  .contact--address { left: 384px; width: 200px; text-align: center; font-size: 10.5px; }

  .web-band {
    position: absolute; left: 0; bottom: 0; width: 100%; height: 43px;
    background: var(--blue);
    color: var(--white); font-size: 13px; letter-spacing: 0.02em;
    display: flex; align-items: center; justify-content: center;
    text-transform: uppercase;
  }

  .city-view {
    position: absolute; left: 0; top: 0; width: 100%; height: 316px;
    background: linear-gradient(180deg, #eef1f5 0%, #dde5ee 45%, #c8d4e2 75%, #b9c8da 100%);
  }
  .card--back .brand {
    position: absolute; left: 0; right: 0; top: 148px;
    text-align: center; font-size: 32px;
  }
</style>
</head>
<body>
<div class="stage">

  <section class="card card--front">
    <div class="brand">Norvane Group</div>

    <div class="holder">
      <div class="holder__name">ELIAS MORROW</div>
      <div class="holder__title">GRAND MANAGER</div>
    </div>

    <div class="skyline-band" role="img" aria-label="Blue-toned photograph of a dense city skyline"></div>

    <svg class="pin" style="left:54px" viewBox="0 0 40 52" aria-hidden="true">
      <path d="M20 0a20 20 0 0 1 8 38.3L20 52l-8-13.7A20 20 0 0 1 20 0z" fill="#3276b5"/>
      <path d="M14 11c1.2-.8 2.4-.4 3 .6l1.4 2.4c.5.9.2 1.8-.6 2.3l-1 .6c.8 2 2.4 3.7 4.4 4.6l.7-1c.5-.8 1.5-1 2.3-.5l2.4 1.5c.9.6 1.2 1.8.5 2.9-1 1.6-2.6 2.2-4.5 1.5-4.6-1.7-8-5.2-9.6-9.8-.6-1.9 0-3.7 1-5.1z" fill="#fff"/>
    </svg>
    <svg class="pin" style="left:255px" viewBox="0 0 40 52" aria-hidden="true">
      <path d="M20 0a20 20 0 0 1 8 38.3L20 52l-8-13.7A20 20 0 0 1 20 0z" fill="#3276b5"/>
      <rect x="9" y="12" width="22" height="15" rx="1.5" fill="none" stroke="#fff" stroke-width="1.8"/>
      <path d="M9.5 13l10.5 8 10.5-8M9.5 26.5l8-7M30.5 26.5l-8-7" fill="none" stroke="#fff" stroke-width="1.6"/>
    </svg>
    <svg class="pin" style="left:462px" viewBox="0 0 40 52" aria-hidden="true">
      <path d="M20 0a20 20 0 0 1 8 38.3L20 52l-8-13.7A20 20 0 0 1 20 0z" fill="#3276b5"/>
      <path d="M20 8a7 7 0 0 1 7 7c0 5-7 13-7 13s-7-8-7-13a7 7 0 0 1 7-7z" fill="#fff"/>
      <circle cx="20" cy="15" r="2.8" fill="#3276b5"/>
    </svg>

    <p class="contact contact--phone">555 - 210 - 418</p>
    <p class="contact contact--email">hello@norvanegroup.com</p>
    <p class="contact contact--address">Westbrook Avenue, Suite 4<br>Halden 20418</p>

    <div class="web-band">norvanegroup.com</div>
  </section>

  <section class="card card--back">
    <div class="city-view" role="img" aria-label="Pale hazy photograph of a city with a tall glass tower and hills behind"></div>
    <div class="brand">Norvane Group</div>
    <div class="web-band">norvanegroup.com</div>
  </section>

</div>
</body>
</html>
```